Willowmere Spa and Beauty Ltd. (Name of business)

I need a business card designed for this new company based out of Toronto Ontario. We specialize in Eyelash Extensions, Manicures and Pedicures, body waxing, massages, laser hair removal and botox treatments. Also offer a variety of products for sale, such as skin cream serums, collagen gel, eye cream, etc. It is a safe relaxing and non-judgemental environnment. Clients are welcome to come be pampered for the half or full day. Many service packages to choose from.

Open 7days per week from 8am to 8pm.

Priscilla Dunmore
Spa Facilitator
Willowmere Spa and Beauty Ltd.
7200 Harcourt St; Suite 1400
Toronto ON K2P 9W4

OFFICE: 416.790.4100
FAX: 416.790.4101
CELL: 416.632.1987
EMAIL: priscilla.dunmore@willowmerespa.com

Target Market(s)

Target market is primarily female ranging from 16 years old to 50 years old.

Industry/Entity Type

Business

Contact Information for Business Card

Priscilla Dunmore
Spa Facilitator
7200 Harcourt St; Suite 1400
Toronto ON K2P 9W4

OFFICE: 416.790.4100
FAX: 416.790.4101
CELL: 416.632.1987

Logo Text

I dont have a logo yet. I would like it simple but sophisticated and modern.

Font styles to use
Serif

Requirements
Must have
• all pertinent details such as company name, logo, name and contact information, services that are offered, including package rates
Nice to have
• Company name and logo prominent. A card that is neat and the information such as address, phone number, fax, email, etc is not too crowded but laid out in an easy to read format.
• Possibly on the back of card - some of the services offered could be listed, as well as professional cream lotions and serums. Hours of operation etc.

```html
<!DOCTYPE html>
<html lang="en">
<head>
<meta charset="utf-8">
<title>Willowmere Spa and Beauty Ltd. — Business Card</title>
<link rel="stylesheet" href="https://fonts.googleapis.com/css2?family=Questrial&family=Oswald:wght@500&display=swap">
<style>
  :root {
    --backdrop: #7a8590;
    --card: #0f141d;
    --gold: #cfae52;
    --gold-light: #e9d38a;
    --ink-light: #e4e4e4;
    --ink-muted: #b9bcc2;
    --text-font: "Questrial", sans-serif;
    --name-font: "Oswald", sans-serif;
  }
  * { margin: 0; padding: 0; box-sizing: border-box; }
  html, body {
    width: 1200px;
    height: 830px;
    overflow: hidden;
    background: var(--backdrop);
  }
  .card {
    position: absolute;
    left: 100px;
    top: 130px;
    width: 1000px;
    height: 571px;
    overflow: hidden;
    background: var(--card);
    font-family: var(--text-font);
    color: var(--ink-light);
  }
  .brand {
    position: absolute;
    left: 230px;
    top: 60px;
    width: 420px;
    text-align: center;
    color: var(--gold);
    font-family: var(--text-font);
  }
  .brand-dot {
    display: block;
    width: 90px;
    height: 90px;
    margin: 0 auto 26px;
    border-radius: 50%;
    background: var(--gold);
  }
  .brand-name {
    font-size: 30px;
    letter-spacing: 1px;
    line-height: 1.2;
  }
  .divider {
    position: absolute;
    left: 40px;
    top: 300px;
    width: 920px;
    height: 2px;
    background: linear-gradient(90deg, var(--ink-light) 0%, var(--gold) 40%, var(--gold-light) 100%);
  }
  .person {
    position: absolute;
    right: 40px;
    top: 250px;
    text-align: right;
  }
  .person-name {
    font-family: var(--name-font);
    font-weight: 500;
    font-size: 26px;
    color: var(--gold);
    line-height: 40px;
  }
  .person-title {
    margin-top: 14px;
    font-size: 22px;
    color: var(--ink-muted);
  }
  .contacts {
    position: absolute;
    left: 490px;
    top: 362px;
    font-size: 20px;
    border-collapse: collapse;
  }
  .contacts td { padding: 3px 0; white-space: nowrap; }
  .contact-label { color: var(--gold); padding-right: 24px !important; }
  .contact-value { color: var(--ink-light); }
  .address {
    position: absolute;
    left: 70px;
    top: 380px;
    font-size: 32px;
    line-height: 1.35;
    color: var(--ink-light);
    font-style: normal;
  }
</style>
</head>
<body>
  <section class="card">
    <div class="brand">
      <span class="brand-dot"></span>
      <div class="brand-name">Willowmere Spa and Beauty Ltd.</div>
    </div>

    <div class="divider"></div>

    <div class="person">
      <div class="person-name">Priscilla Dunmore</div>
      <div class="person-title">Spa Facilitator</div>
    </div>

    <table class="contacts">
      <tr><td class="contact-label">Office</td><td class="contact-value">416.790.4100</td></tr>
      <tr><td class="contact-label">Fax</td><td class="contact-value">416.790.4101</td></tr>
      <tr><td class="contact-label">Cell</td><td class="contact-value">416.632.1987</td></tr>
      <tr><td class="contact-label">Email</td><td class="contact-value">priscilla.dunmore@willowmerespa.com</td></tr>
    </table>

    <address class="address">
      7200 Harcourt St<br>
      Suite 1400<br>
      Toronto ON K2P 9W4
    </address>
  </section>
</body>
</html>
```